Business card design needed

Our modern electrical contracting company requires business card design utilising our logo and incorporating our tag line "Service when you need it". We specialise in assisting our customers 24/7 offering a breakdown service.

Industry/Entity Type

Electrical

Contact Information for Business Card

Marcus Penhale, Electrical contractor,Tel: (08) 8456 3071, Fax: (08) 8679 4315, Mob 0438 562 740, Email: marcus.penhale@brightwirepower.com.au, Web: www.brightwirepower.com.au

Requirements
Must have
• we require a 2 sided card.
Front- Logo, tag line and contact information.
Rear- service when you need it! Call now for our 24/7 breakdown service

```html
<!DOCTYPE html>
<html lang="en">
<head>
<meta charset="utf-8">
<title>Brightwire Power – Business Card</title>
<link rel="stylesheet" href="https://fonts.googleapis.com/css2?family=Arimo:ital,wght@0,700;1,400&family=Tinos:wght@400;700&family=Alfa+Slab+One&display=swap">
<style>
  :root {
    --bg: #dfe3e6;
    --card: #f7f7f8;
    --brand-blue: #2d56a8;
    --band-blue: #4b78c8;
    --ink: #1b1b1b;
    --muted: #6d6f74;
    --ghost: #e6e6ea;
    --ghost-edge: #d9d9df;
  }
  * { box-sizing: border-box; margin: 0; padding: 0; }
  html, body { width: 1200px; height: 960px; overflow: hidden; }
  body {
    background: var(--bg);
    position: relative;
    font-family: "Tinos", "Times New Roman", serif;
    color: var(--ink);
  }
  .card {
    position: absolute;
    left: 250px;
    width: 700px;
    height: 400px;
    background: var(--card);
    overflow: hidden;
    box-shadow: 0 2px 10px rgba(0,0,0,0.12);
  }
  .card--front { top: 60px; }
  .card--back { top: 500px; }

  .ghost-disc {
    position: absolute;
    border-radius: 50%;
    background: radial-gradient(circle at 40% 40%, #f1f1f4 0%, var(--ghost) 60%, var(--ghost-edge) 100%);
  }
  .card--front .ghost-disc { width: 440px; height: 440px; left: -120px; top: 20px; }
  .card--back .ghost-disc { width: 300px; height: 300px; left: 440px; top: 40px; }

  .brand-mark {
    position: absolute;
    left: 50px; top: 48px;
    width: 90px; height: 90px;
    border-radius: 50%;
    background: var(--brand-blue);
    box-shadow: 0 10px 8px -6px rgba(0,0,0,0.35);
  }
  .brand {
    position: absolute;
    right: 26px; top: 42px;
    text-align: right;
  }
  .brand__name {
    font-family: "Arimo", Arial, sans-serif;
    font-weight: 700;
    font-size: 28px;
    letter-spacing: 0.5px;
    color: var(--brand-blue);
    line-height: 1;
  }
  .brand__tagline {
    font-family: "Arimo", Arial, sans-serif;
    font-style: italic;
    font-size: 15px;
    color: var(--muted);
    letter-spacing: 1px;
    margin-top: 3px;
    padding-right: 14px;
  }
  .holder {
    position: absolute;
    left: 398px; right: 26px; top: 124px;
  }
  .holder__name {
    background: var(--band-blue);
    color: #fff;
    font-family: "Alfa Slab One", "Times New Roman", serif;
    font-size: 20px;
    letter-spacing: 1px;
    text-align: center;
    height: 30px;
    line-height: 31px;
  }
  .holder__role {
    text-align: right;
    font-size: 14px;
    margin-top: 6px;
  }
  .contacts {
    position: absolute;
    left: 360px; top: 226px;
    list-style: none;
  }
  .contacts li {
    display: flex;
    align-items: center;
    height: 27px;
    font-size: 16px;
    white-space: nowrap;
  }
  .contacts svg { width: 20px; height: 20px; margin-right: 8px; flex: none; }

  .back-message {
    position: absolute;
    left: 0; right: 0; top: 168px;
    text-align: center;
    font-size: 20px;
    line-height: 1.1;
    letter-spacing: 0.6px;
  }
</style>
</head>
<body>

<section class="card card--front" aria-label="Card front">
  <div class="ghost-disc"></div>
  <div class="brand-mark"></div>
  <header class="brand">
    <div class="brand__name">BRIGHTWIRE POWER</div>
    <div class="brand__tagline">"Service when you need it"</div>
  </header>
  <div class="holder">
    <div class="holder__name">MARCUS PENHALE</div>
    <div class="holder__role">Electrical contractor</div>
  </div>
  <ul class="contacts">
    <li>
      <svg viewBox="0 0 22 22"><rect x="1" y="1" width="20" height="20" rx="6" fill="#3d8fd6"/><rect x="7.5" y="4" width="7" height="14" rx="1.5" fill="none" stroke="#fff" stroke-width="1.4"/><line x1="9.5" y1="15.5" x2="12.5" y2="15.5" stroke="#fff" stroke-width="1.2"/></svg>
      0438 562 740
    </li>
    <li>
      <svg viewBox="0 0 22 22"><circle cx="11" cy="11" r="9.5" fill="#fff" stroke="#222" stroke-width="1.5"/><path d="M7 6.5c-1 1 -.6 3.5 1.8 6.2s5 3.3 6.2 2.3l.8-1.1-2.2-1.6-1 .9c-1-.4-2.8-2.2-3.2-3.2l.9-1-1.6-2.2z" fill="#222"/></svg>
      (08) 8456 3071
    </li>
    <li>
      <svg viewBox="0 0 22 22"><rect x="1" y="1" width="20" height="20" rx="3" fill="#c9cbd0"/><rect x="6" y="3.5" width="10" height="6" fill="#fff" stroke="#666" stroke-width="0.8"/><rect x="4" y="9.5" width="14" height="8" rx="1" fill="#8a8d93"/><rect x="6.5" y="14" width="9" height="2" fill="#fff"/></svg>
      (08) 8679 4315
    </li>
    <li>
      <svg viewBox="0 0 22 22"><circle cx="11" cy="11" r="10" fill="#2f4fa0"/><text x="11" y="15.5" text-anchor="middle" font-family="Arimo, Arial, sans-serif" font-size="13" font-weight="700" fill="#fff">@</text></svg>
      marcus.penhale@brightwirepower.com.au
    </li>
    <li>
      <svg viewBox="0 0 22 22"><rect x="1" y="1" width="20" height="20" rx="3" fill="#111"/><text x="11" y="14" text-anchor="middle" font-family="Arimo, Arial, sans-serif" font-size="6.5" font-weight="700" fill="#fff">www</text></svg>
      www.brightwirepower.com.au
    </li>
  </ul>
</section>

<section class="card card--back" aria-label="Card back">
  <div class="ghost-disc"></div>
  <p class="back-message">Service when you need it!<br>Call now for our 24/7 breakdown service</p>
</section>

</body>
</html>
```